Lawn mowing business card design

We need a business card design for our lawn mowing and gardening business which is located in the Northern Beaches of Sydney. Our business name is Meadowline Turf and our logo is predominantly green and yellow in color. Please see our website at www.meadowlineturf.com.au for design ideas. The business targets young professionals and older clientele. As such the font should be easy to read, but I also want the business card to be colorful and stand out.

Target Market(s)

young professionals

Industry/Entity Type

Lawn Care

Contact Information for Business Card

Meadowline Turf, Gareth Pellow, 0478559201, www.meadowlineturf.com.au, email: meadowlineturf@mailbox-example.com

Font styles to use
Serif

Colors
9bcb3b
fbed22

Requirements
Must have
• Must include the details listed above. Must include the attached logo.
Nice to have
• Logo attached with two copies. The logo without any writing is high quality, please feel free to be creative with the text stating our business name "Meadowline Turf" using this file.

```html
<!DOCTYPE html>
<html lang="en">
<head>
<meta charset="utf-8">
<title>Meadowline Turf – Business Card</title>
<link rel="stylesheet" href="https://fonts.googleapis.com/css2?family=Arimo:wght@400;700&display=swap">
<style>
  :root {
    --page-bg: #ecebe6;
    --green-deep: #1c6e3c;
    --green-mid: #2f8f4e;
    --green-brand: #2e9b46;
    --green-lime: #9bcb3b;
    --green-soft: #6aa744;
    --yellow: #fbed22;
    --ink: #222222;
    --ink-soft: #4a4a4a;
    --card-white: #ffffff;
    --card-shade: #e9e9e9;
  }
  * { box-sizing: border-box; margin: 0; padding: 0; }
  html, body { width: 1200px; height: 950px; overflow: hidden; }
  body {
    background: var(--page-bg);
    font-family: "Arimo", Arial, sans-serif;
    display: flex;
    flex-direction: column;
    align-items: center;
    justify-content: center;
    gap: 30px;
  }
  .card {
    position: relative;
    width: 700px;
    height: 428px;
    overflow: hidden;
    box-shadow: 0 6px 18px rgba(0,0,0,0.18);
  }
  .card-art { position: absolute; inset: 0; width: 100%; height: 100%; }

  /* Front */
  .card-front { background: linear-gradient(160deg, var(--card-white) 45%, var(--card-shade) 100%); }
  .holder {
    position: absolute;
    left: 52px;
    top: 150px;
  }
  .holder-name {
    color: var(--green-brand);
    font-weight: 700;
    font-size: 27px;
    letter-spacing: 0.2px;
  }
  .holder-role {
    color: var(--ink);
    font-size: 18px;
    margin-top: 6px;
  }
  .contact-list {
    list-style: none;
    margin-top: 16px;
  }
  .contact-item {
    display: flex;
    align-items: center;
    gap: 10px;
    color: var(--ink-soft);
    font-size: 19px;
    line-height: 30px;
  }
  .contact-icon { width: 17px; height: 17px; flex: none; }

  .brand {
    position: absolute;
    display: flex;
    align-items: center;
    gap: 12px;
  }
  .brand-front { left: 420px; top: 140px; }
  .brand-mark {
    width: 26px;
    height: 26px;
    background: var(--green-lime);
  }
  .brand-name {
    font-weight: 700;
    font-size: 28px;
    color: var(--green-deep);
  }

  /* Back */
  .card-back {
    background: linear-gradient(125deg, var(--green-mid) 0%, var(--green-deep) 70%);
  }
  .brand-back { left: 50%; top: 170px; transform: translateX(-50%); }
  .brand-back .brand-mark { background: var(--yellow); }
  .brand-back .brand-name { color: var(--card-white); font-size: 34px; }
  .back-web {
    position: absolute;
    left: 0; right: 0;
    top: 238px;
    text-align: center;
    color: rgba(255,255,255,0.55);
    font-size: 17px;
    letter-spacing: 0.5px;
  }
</style>
</head>
<body>

  <section class="card card-back" aria-label="Card back">
    <svg class="card-art" viewBox="0 0 700 428" aria-hidden="true">
      <polygon points="420,0 700,0 700,428 560,428" fill="rgba(255,255,255,0.06)"/>
    </svg>
    <div class="brand brand-back">
      <span class="brand-mark"></span>
      <span class="brand-name">Meadowline Turf</span>
    </div>
    <p class="back-web">www.meadowlineturf.com.au</p>
  </section>

  <section class="card card-front" aria-label="Card front">
    <svg class="card-art" viewBox="0 0 700 428" aria-hidden="true">
      <polygon points="0,0 240,0 0,100" fill="var(--green-lime)"/>
      <polygon points="240,0 256,0 0,107 0,100" fill="var(--green-mid)"/>
      <polygon points="700,300 700,428 400,428" fill="var(--green-soft)"/>
      <polygon points="700,290 700,300 400,428 378,428" fill="var(--green-mid)"/>
    </svg>

    <div class="holder">
      <h1 class="holder-name">Gareth Pellow</h1>
      <p class="holder-role">President</p>
      <ul class="contact-list">
        <li class="contact-item">
          <svg class="contact-icon" viewBox="0 0 24 24" aria-hidden="true"><path fill="var(--green-brand)" d="M6.6 10.8a15.1 15.1 0 0 0 6.6 6.6l2.2-2.2a1 1 0 0 1 1-.25 11.4 11.4 0 0 0 3.6.57 1 1 0 0 1 1 1V20a1 1 0 0 1-1 1A17 17 0 0 1 3 4a1 1 0 0 1 1-1h3.5a1 1 0 0 1 1 1c0 1.25.2 2.45.57 3.57a1 1 0 0 1-.25 1z"/></svg>
          0478559201
        </li>
        <li class="contact-item">
          <svg class="contact-icon" viewBox="0 0 24 24" aria-hidden="true"><rect x="2" y="5" width="20" height="14" rx="1.5" fill="var(--green-brand)"/><path d="M3 6l9 7 9-7" fill="none" stroke="#fff" stroke-width="1.8"/></svg>
          meadowlineturf@mailbox-example.com
        </li>
        <li class="contact-item">
          <svg class="contact-icon" viewBox="0 0 24 24" aria-hidden="true"><path fill="var(--green-brand)" d="M12 2a7 7 0 0 0-7 7c0 5.2 7 13 7 13s7-7.8 7-13a7 7 0 0 0-7-7zm0 9.5A2.5 2.5 0 1 1 12 6.5a2.5 2.5 0 0 1 0 5z"/></svg>
          www.meadowlineturf.com.au
        </li>
      </ul>
    </div>

    <div class="brand brand-front">
      <span class="brand-mark"></span>
      <span class="brand-name">Meadowline Turf</span>
    </div>
  </section>

</body>
</html>
```